Bref créative
R.T. M&P Stationary
Simple
Odel Krasniak
7281 Porravel Blvd.
Suite 382
North Hollywood, CA 91602
odel@tinmarrowseek.com
www.tinmarrowseek.com

```html
<!DOCTYPE html>
<html lang="en">
<head>
<meta charset="utf-8">
<title>R.T. M&amp;P Stationary</title>
<link rel="stylesheet" href="https://fonts.googleapis.com/css2?family=Montserrat:wght@700&family=Libre+Baskerville&family=Open+Sans:wght@400;700&display=swap">
<style>
  :root {
    --backdrop: #2b2a29;
    --card: #6a6b6d;
    --card-dark: #5f6062;
    --gold: #d9c98a;
    --gold-deep: #bfa865;
    --ink-light: #f1efe8;
    --faint: rgba(255, 255, 255, 0.06);
  }
  * { margin: 0; padding: 0; box-sizing: border-box; }
  html, body { width: 1200px; height: 874px; overflow: hidden; }
  body {
    background: var(--backdrop);
    position: relative;
    font-family: "Open Sans", sans-serif;
  }
  .card {
    position: absolute;
    top: 282px;
    width: 540px;
    height: 309px;
    background: var(--card);
    overflow: hidden;
  }
  .card--front { left: 40px; }
  .card--back { left: 620px; background: var(--card-dark); }

  .brand {
    display: flex;
    align-items: center;
    gap: 12px;
    color: var(--gold);
    font-family: "Montserrat", sans-serif;
    font-weight: 700;
    letter-spacing: 0.02em;
  }
  .brand__square {
    display: block;
    background: var(--gold);
  }
  .card--front .brand {
    position: absolute;
    left: 50%;
    top: 50%;
    transform: translate(-50%, -50%);
    font-size: 34px;
  }
  .card--front .brand__square { width: 40px; height: 40px; }

  .card--back .brand {
    position: absolute;
    left: 34px;
    top: 62px;
    font-size: 24px;
  }
  .card--back .brand__square { width: 30px; height: 30px; }

  .back-watermark {
    position: absolute;
    right: -18px;
    top: 20px;
    font-family: "Montserrat", sans-serif;
    font-weight: 700;
    font-size: 110px;
    color: var(--faint);
    line-height: 1;
  }

  .person-name {
    position: absolute;
    left: 60px;
    top: 168px;
    font-family: "Libre Baskerville", serif;
    font-size: 22px;
    color: var(--gold);
  }
  .contact {
    position: absolute;
    left: 60px;
    top: 206px;
    font-size: 10.5px;
    line-height: 17px;
    color: var(--ink-light);
  }
  .contact b { font-weight: 700; }
  .contact .sep { margin: 0 6px; color: var(--gold); }

  .corner-accent {
    position: absolute;
    left: 0;
    bottom: 0;
  }
</style>
</head>
<body>
  <section class="card card--front" aria-label="Card front">
    <div class="brand"><span class="brand__square"></span>R.T. M&amp;P</div>
  </section>

  <section class="card card--back" aria-label="Card back">
    <div class="back-watermark" aria-hidden="true">R.T. M&amp;P</div>
    <div class="brand"><span class="brand__square"></span>R.T. M&amp;P</div>
    <h1 class="person-name">Odel Krasniak</h1>
    <div class="contact">
      <p>7281 Porravel Blvd., Suite 382, North Hollywood, CA 91602</p>
      <p><b>Toll Free</b> 888-402-7715<span class="sep">|</span><b>P</b> 818-554-3091<span class="sep">|</span><b>F</b> 818-554-3092</p>
      <p><b>E</b> odel@tinmarrowseek.com<span class="sep">|</span><b>W</b> www.tinmarrowseek.com</p>
    </div>
    <svg class="corner-accent" width="60" height="120" viewBox="0 0 60 120" aria-hidden="true">
      <polygon points="0,20 40,60 0,100" fill="var(--gold)"/>
      <polygon points="0,70 30,100 0,120" fill="var(--gold-deep)"/>
    </svg>
  </section>
</body>
</html>
```